Three diagrams for research framework required

I need a three diagrams produced to capture principles of a research approach.<br/><br/>The first is a cycle diagram, produced to capture seven principles of a research framework. My idea is to be similar to the example attached, but incorporate seven principles and the koru (fern) imagery (example attached) that relates to our logo (also attached). The centre piece of the diagram should be labelled Open Meadow Wordcraft Method.<br/><br/>The seven principles are:<br/>1. Thinking proactively<br/>2. Ensuring positive learning experiences<br/>3. Fostering positive collaborations<br/>4. Providing constructive reporting<br/>5. Prioritising whānau engagement<br/>6. Being culturally responsive<br/>7. Maximizing protective factors<br/><br/>The second and third diagram should be updated versions of the attached, so all three diagrams look related. See diagrams attached that require updating (diagram 2 and 3).<br/><br/>The three diagrams need to be cohesive and clearly related aesthetically. All final files need to be produced in Adobe Photoshop or InDesign, so minor edits to text can easily be made in future.

Industry/Entity Type

Education

Font styles to use
Sans Serif

Colors

Designer to choose colors to be used in the design.

Requirements
Must have
• Clean design, easy to read and understand.
Should not have
• Complicated, overly busy design.

```html
<!DOCTYPE html>
<html lang="en">
<head>
<meta charset="utf-8">
<title>Open Meadow Wordcraft Method – Framework Diagram</title>
<link href="https://fonts.googleapis.com/css2?family=Cinzel:wght@400&family=Cormorant+Garamond:ital@1&family=Open+Sans:ital,wght@0,400;0,600;0,700;1,400&display=swap" rel="stylesheet">
<style>
  :root {
    --page: #dcdcdc;
    --paper: #ffffff;
    --leaf: #7aab35;
    --plum: #77527f;
    --lime: #abcc04;
    --slate: #878daf;
    --maroon: #5a0f27;
    --ink: #3a2a2a;
    --partner: #dedede;
    --badge: #b9b9b9;
  }
  html, body { margin: 0; padding: 0; overflow: hidden; }
  body { width: 1200px; height: 729px; background: var(--page); position: relative; font-family: "Open Sans", sans-serif; }
  .panel { position: absolute; background: var(--paper); }
  .panel--brand { left: 43px; top: 25px; width: 260px; height: 678px; }
  .panel--diagram { left: 345px; top: 25px; width: 811px; height: 678px; }

  .brand-mark { position: absolute; left: 80px; top: 243px; width: 100px; height: 100px; border-radius: 50%; background: var(--leaf); }
  .brand-name { position: absolute; left: 0; right: 0; top: 378px; margin: 0; text-align: center;
    font-family: "Cinzel", serif; font-weight: 400; font-size: 18px; line-height: 20px; color: var(--ink);
    text-transform: uppercase; letter-spacing: 0.2px; }
  .brand-maori { position: absolute; left: 0; right: 0; top: 418px; margin: 0; text-align: center;
    font-family: "Cormorant Garamond", serif; font-style: italic; font-size: 17px; line-height: 20px; color: var(--leaf); }
  .brand-tagline { position: absolute; left: 0; right: 0; top: 446px; margin: 0; text-align: center;
    font-family: "Open Sans", sans-serif; font-style: italic; font-size: 7px; color: var(--maroon); }

  .partner { position: absolute; left: 32px; top: 612px; width: 197px; height: 47px; background: var(--partner);
    display: flex; align-items: center; gap: 5px; padding: 0 5px; box-sizing: border-box; }
  .partner-uni { display: flex; align-items: center; gap: 3px; flex: none; width: 54px;
    font-size: 7px; line-height: 8px; color: #333; }
  .partner-badge { width: 10px; height: 10px; background: var(--badge); flex: none; }
  .partner-text { font-size: 8.5px; line-height: 11px; color: #333; }
  .partner-text small { display: block; font-size: 6px; letter-spacing: 1px; }

  .diagram { position: absolute; left: 0; top: 0; width: 1200px; height: 729px; }
  .label { font-family: "Open Sans", sans-serif; font-weight: 700; fill: #fff; font-size: 27px; text-anchor: middle; }
  .label--core { font-size: 37px; }
</style>
</head>
<body>
  <section class="panel panel--brand">
    <div class="brand-mark" aria-hidden="true"></div>
    <h1 class="brand-name">Open Meadow<br>Wordcraft Method</h1>
    <p class="brand-maori">Te Ara Kupu Hou</p>
    <p class="brand-tagline">Building foundational skills to foster succes for early learners</p>
    <div class="partner">
      <div class="partner-uni"><span class="partner-badge" aria-hidden="true"></span>Riverbend University</div>
      <div class="partner-text"><small>Te Pā Tamariki</small>Child Growth Research Centre</div>
    </div>
  </section>

  <section class="panel panel--diagram"></section>

  <svg class="diagram" viewBox="0 0 2100 1275" aria-label="Framework cycle diagram">
    <defs>
      <clipPath id="clip-plum"><circle cx="1446" cy="506" r="403"/></clipPath>
      <clipPath id="clip-left"><rect x="0" y="0" width="1420" height="1275"/></clipPath>
      <mask id="mask-slate-over-lime">
        <circle cx="1446" cy="768" r="403" fill="#fff"/>
        <circle cx="1153" cy="506" r="403" fill="#000" clip-path="url(#clip-left)"/>
      </mask>
    </defs>

    <g class="rings">
      <circle cx="1153" cy="768" r="403" fill="var(--slate)"/>
      <circle cx="1446" cy="768" r="403" fill="var(--lime)"/>
      <circle cx="1153" cy="506" r="403" fill="var(--leaf)"/>
      <circle cx="1446" cy="506" r="403" fill="var(--plum)"/>
      <circle cx="1446" cy="768" r="403" fill="var(--lime)" clip-path="url(#clip-plum)"/>
      <circle cx="1153" cy="768" r="403" fill="var(--slate)" mask="url(#mask-slate-over-lime)"/>
    </g>

    <g class="cycle-arrows" fill="none" stroke="#fff" stroke-width="16">
      <path d="M1042 438 Q1052 405 1080 390"/>
      <polygon points="1068,372 1116,382 1076,430" fill="#fff" stroke="none"/>
      <path d="M1502 385 Q1530 405 1538 420"/>
      <polygon points="1508,420 1564,418 1550,462" fill="#fff" stroke="none"/>
      <path d="M1558 830 Q1545 855 1525 866"/>
      <polygon points="1522,836 1478,878 1526,892" fill="#fff" stroke="none"/>
      <path d="M1114 895 Q1085 880 1075 858"/>
      <polygon points="1050,862 1064,818 1106,860" fill="#fff" stroke="none"/>
    </g>

    <circle class="core-ring" cx="1300" cy="636" r="210" fill="#fff"/>
    <circle class="core" cx="1300" cy="636" r="198" fill="var(--maroon)"/>

    <text class="label label--core" x="1300" y="556">Response to</text>
    <text class="label label--core" x="1300" y="601">Intervention</text>
    <text class="label label--core" x="1300" y="646">framework for</text>
    <text class="label label--core" x="1300" y="691">Foundational</text>
    <text class="label label--core" x="1300" y="736">Learning Skill</text>

    <text class="label" x="1448" y="226">MANA ENHANCING</text>
    <text class="label" x="1448" y="260">WHANAU</text>
    <text class="label" x="1448" y="293">ENGAGEMENT</text>

    <text class="label" x="934" y="437">TEACHER</text>
    <text class="label" x="938" y="470">PROFESSIONAL</text>
    <text class="label" x="934" y="503">LEARNING</text>
    <text class="label" x="938" y="537">AND</text>
    <text class="label" x="941" y="570">DEVELOPMENT</text>

    <text class="label" x="1687" y="740">MONITORING</text>
    <text class="label" x="1687" y="773">ASSESSMENTS</text>

    <text class="label" x="1147" y="997">TEACHER</text>
    <text class="label" x="1151" y="1031" xml:space="preserve">RESOURCES  FOR EARLY LITERACY</text>
    <text class="label" x="1151" y="1064">SUCCES</text>
  </svg>
</body>
</html>
```